Law Firm Letterhead

We are looking for a letterhead for our military/veterans law firm. We like simplicity and clean, modern, flat, uncluttered designs. Our logo font is DIN 1451, and our website/business card info font is Helvetica Neue.

Required Information:

- Logo/Graphic: Please see attached logo / business card for ideas. Please also review firm website.

- Motto: A law firm for service members and veterans

- Web Address: www.harborlinecounsel.com

- Email: info@harborlinecounsel.com

- Phone: 866-402-1953

Colors: We prefer either a blue/grey or an all-blue color scheme. The blue in our logo is #336699.

Please DO NOT submit more than 3 designs. Spamming designs with only minor changes between the designs is not appreciated. We can evaluate your quality and direction by your best 1 or 2 designs.

Thank you!

```html
<!DOCTYPE html>
<html lang="en">
<head>
<meta charset="utf-8">
<title>Harborline Counsel Letterhead</title>
<link rel="stylesheet" href="https://fonts.googleapis.com/css2?family=Barlow+Condensed:wght@500&family=Barlow:wght@500&display=swap">
<style>
  :root {
    --brand-blue: #336699;
    --band-blue: #33679a;
    --arc-grey: #9a9a9c;
    --ink: #111111;
    --paper: #ffffff;
    --backdrop: #e9e9eb;
    --rule: #8a8a8a;
  }
  html, body {
    margin: 0;
    padding: 0;
    width: 943px;
    height: 1200px;
    overflow: hidden;
    background: var(--backdrop);
  }
  .letterhead {
    position: absolute;
    left: 54px;
    top: 90px;
    width: 805px;
    height: 1041px;
    background: var(--paper);
    box-shadow: 0 2px 8px rgba(0,0,0,0.12);
    overflow: hidden;
  }
  .firm-name {
    position: absolute;
    left: 18px;
    top: 26px;
    margin: 0;
    font-family: "Barlow Condensed", "Arial Narrow", sans-serif;
    font-weight: 500;
    color: var(--brand-blue);
    font-size: 36px;
    line-height: 30px;
    letter-spacing: 0.5px;
    text-transform: uppercase;
  }
  .firm-name .firm-name__second {
    display: block;
    font-size: 22px;
    line-height: 24px;
    letter-spacing: 4px;
    padding-left: 48px;
  }
  .contact {
    position: absolute;
    left: 544px;
    top: 26px;
    margin: 0;
    padding: 4px 0 4px 9px;
    border-left: 1px solid var(--rule);
    list-style: none;
    font-family: "Barlow", "Helvetica Neue", Arial, sans-serif;
    font-weight: 500;
    font-size: 14.5px;
    line-height: 22px;
    color: var(--ink);
  }
  .contact__label {
    color: var(--brand-blue);
    margin-right: 3px;
  }
  .footer-band {
    position: absolute;
    left: 0;
    bottom: 0;
    width: 805px;
    height: 85px;
  }
  .motto {
    position: absolute;
    left: 0;
    right: 0;
    bottom: 22px;
    margin: 0;
    text-align: center;
    font-family: "Barlow", "Helvetica Neue", Arial, sans-serif;
    font-weight: 500;
    font-size: 16px;
    letter-spacing: 1px;
    color: var(--paper);
  }
</style>
</head>
<body>
  <main class="letterhead">
    <h1 class="firm-name">Harborline<span class="firm-name__second">Counsel</span></h1>

    <ul class="contact">
      <li><span class="contact__label">p:</span>866-402-1953</li>
      <li><span class="contact__label">e:</span>info@harborlinecounsel.com</li>
      <li><span class="contact__label">w:</span>www.harborlinecounsel.com</li>
    </ul>

    <svg class="footer-band" viewBox="0 0 805 85" aria-hidden="true">
      <path d="M0 54 Q402 -12 805 52" fill="none" stroke="var(--arc-grey)" stroke-width="3"/>
      <path d="M0 61 Q402 -6 805 61 L805 85 L0 85 Z" fill="var(--band-blue)"/>
    </svg>
    <p class="motto">A law firm for service members and veterans</p>
  </main>
</body>
</html>
```